Looking for fresh and exciting business card design that is simple and yet eye catching and impactfu

I am starting my own independent Marketing Communications consultancy with aim to service a small group of clients. Focus on aviation, travel and hospitality industries. Name of the consultancy is RQB BizLink or RQB Marketing Communications. Basic content of the card will be
RQB Marketing Communications / RQB BizLink
Greta Lund Okafor
Email
Mobile
Website

Target Market(s)

Aviation, travel and hospitality industries

Industry/Entity Type

Travel

Contact Information for Business Card

Greta Lund Okafor
Consultant
gretalok@mailbrook.example
Mobile : +86 1529 804 2617
Skype: gretabluepebble

Font styles to use
Sans Serif
Script

Requirements
Must have
• Professional look and feel.
Nice to have
• Fresh, contrast. I don't have a logo so using the company name to create a focal point.
Should not have
• Too many colors.

```html
<!DOCTYPE html>
<html lang="en">
<head>
<meta charset="utf-8">
<title>RQB Marketing Communications – Business Card</title>
<link rel="stylesheet" href="https://fonts.googleapis.com/css2?family=Arimo:wght@400;700&display=swap">
<style>
  :root {
    --card-slate: #7f929c;
    --card-slate-dark: #74868f;
    --text-white: #ffffff;
    --dot-white: rgba(255, 255, 255, 0.9);
    --globe-light: #6fa8e6;
    --globe-deep: #1b3f8f;
    --globe-rim: #c9d0d6;
  }
  html, body {
    margin: 0;
    padding: 0;
    width: 1200px;
    height: 702px;
    overflow: hidden;
    background: var(--card-slate);
  }
  .card {
    position: relative;
    width: 1200px;
    height: 702px;
    overflow: hidden;
    font-family: "Arimo", Arial, sans-serif;
    color: var(--text-white);
  }
  .card__backdrop {
    position: absolute;
    inset: 0;
    background: radial-gradient(ellipse at 68% 42%, var(--card-slate) 0%, var(--card-slate-dark) 100%);
  }
  .brand {
    position: absolute;
    left: 84px;
    top: 168px;
    width: 440px;
    text-align: center;
  }
  .brand__name {
    margin: 0;
    font-size: 76px;
    font-weight: 700;
    line-height: 1;
    letter-spacing: 3px;
  }
  .brand__tagline {
    margin: 1px 0 0;
    font-size: 28px;
    font-weight: 700;
    line-height: 1;
    letter-spacing: 1px;
    white-space: nowrap;
  }
  .brand__divider {
    position: absolute;
    left: 216px;
    top: 316px;
    width: 176px;
    height: 8px;
    border-radius: 4px;
    background: linear-gradient(90deg, rgba(255,255,255,0.2), rgba(255,255,255,0.85) 50%, rgba(255,255,255,0.2));
  }
  .brand__globe {
    position: absolute;
    left: 214px;
    top: 347px;
    width: 180px;
    height: 180px;
  }
  .rule-vertical {
    position: absolute;
    left: 554px;
    top: 75px;
    width: 0;
    height: 556px;
    border-left: 3px dotted var(--dot-white);
  }
  .rule-horizontal {
    position: absolute;
    left: 570px;
    top: 262px;
    width: 586px;
    height: 0;
    border-top: 3px dotted var(--dot-white);
  }
  .person {
    position: absolute;
    left: 632px;
    top: 204px;
    display: flex;
    align-items: center;
    white-space: nowrap;
  }
  .person__name {
    margin: 0;
    font-size: 42px;
    font-weight: 400;
    line-height: 1;
  }
  .person__role {
    margin: 0 0 0 12px;
    padding-left: 10px;
    border-left: 2px solid var(--text-white);
    font-size: 25px;
    line-height: 38px;
  }
  .contact {
    position: absolute;
    left: 632px;
    top: 292px;
    margin: 0;
    font-size: 26px;
    line-height: 37px;
    white-space: nowrap;
  }
  .contact__row {
    display: flex;
  }
  .contact__label {
    width: 102px;
    margin: 0;
  }
  .contact__value {
    margin: 0;
  }
</style>
</head>
<body>
<div class="card">
  <div class="card__backdrop" role="img" aria-label="Slate grey backdrop with faint sweeping globe lines"></div>

  <div class="brand">
    <p class="brand__name">RQB</p>
    <p class="brand__tagline">Marketing Communications</p>
  </div>
  <div class="brand__divider" role="img" aria-label="Decorative ornament divider"></div>
  <svg class="brand__globe" viewBox="0 0 180 180" role="img" aria-label="Glossy blue globe illustration">
    <defs>
      <radialGradient id="globe-fill" cx="45%" cy="35%" r="70%">
        <stop offset="0%" stop-color="var(--globe-light)"/>
        <stop offset="100%" stop-color="var(--globe-deep)"/>
      </radialGradient>
    </defs>
    <circle cx="90" cy="90" r="86" fill="var(--globe-rim)"/>
    <circle cx="90" cy="90" r="78" fill="url(#globe-fill)"/>
  </svg>

  <div class="rule-vertical"></div>
  <div class="rule-horizontal"></div>

  <div class="person">
    <h1 class="person__name">Greta Lund Okafor</h1>
    <p class="person__role">Consultant</p>
  </div>

  <dl class="contact">
    <div class="contact__row"><dt class="contact__label">Email:</dt><dd class="contact__value">gretalok@mailbrook.example</dd></div>
    <div class="contact__row"><dt class="contact__label">Mobile:</dt><dd class="contact__value">+86 1529 804 2617</dd></div>
    <div class="contact__row"><dt class="contact__label">Skype:</dt><dd class="contact__value">gretabluepebble</dd></div>
  </dl>
</div>
</body>
</html>
```